Stationery Design for Consulting Company
Orvel Partners
Creative Brief
Professional
Tomas Wenholt
Director
Orvel Partners LLC 48215 Ridgefern Road Dunmore, DE 19872 USA
tomas@orvel-advisory.com
www.orvel-advisory.com
Maybe just a larger logo in the middle unless you have better ideas. I'm open to suggestions.

```html
<!DOCTYPE html>
<html lang="en">
<head>
<meta charset="utf-8">
<title>Orvel Partners — Business Card</title>
<link href="https://fonts.googleapis.com/css2?family=Montserrat:wght@400;500;600;700&display=swap" rel="stylesheet">
<style>
  :root {
    --stage: #e6e6e4;
    --charcoal: #2b2b2b;
    --gold: #f0a828;
    --paper: #ffffff;
    --ink: #3a3a3a;
    --muted: #7a7a7a;
    --rule: #d7d7d7;
  }
  * { box-sizing: border-box; margin: 0; padding: 0; }
  html, body { width: 1200px; height: 754px; overflow: hidden; }
  body {
    background: var(--stage);
    font-family: "Montserrat", sans-serif;
    position: relative;
  }
  .card {
    position: absolute;
    width: 520px;
    height: 298px;
    border-radius: 3px;
    box-shadow: 0 6px 18px rgba(0,0,0,0.18);
    overflow: hidden;
  }
  /* Back side */
  .card-back {
    left: 100px; top: 90px;
    background: var(--charcoal);
    display: flex; align-items: center; justify-content: center;
  }
  .brand {
    display: flex; flex-direction: column; align-items: center; gap: 10px;
  }
  .brand-row { display: flex; align-items: center; gap: 14px; white-space: nowrap; }
  .brand-mark { width: 22px; height: 22px; background: var(--gold); flex: none; }
  .brand-name {
    font-weight: 600; color: var(--gold);
    font-size: 32px; letter-spacing: 0.5px; line-height: 1;
  }
  .brand-tagline {
    font-size: 8px; letter-spacing: 3px; text-transform: uppercase;
    color: var(--muted); white-space: nowrap;
    border-top: 1px solid #555; padding-top: 6px;
  }
  /* Front side */
  .card-front {
    left: 580px; top: 366px;
    background: var(--paper);
  }
  .front-brand {
    position: absolute; left: 30px; top: 104px;
    display: flex; flex-direction: column; align-items: flex-start; gap: 7px;
  }
  .front-brand .brand-name { font-size: 19px; }
  .front-brand .brand-mark { width: 14px; height: 14px; }
  .front-brand .brand-row { gap: 9px; }
  .front-brand .brand-tagline {
    font-size: 5.5px; letter-spacing: 1.6px; border-top-color: var(--rule);
  }
  .contact {
    position: absolute; left: 300px; top: 34px;
    color: var(--ink);
  }
  .person-name {
    font-size: 12px; font-weight: 600; letter-spacing: 1px;
    text-transform: uppercase;
  }
  .person-role { font-size: 8px; color: var(--muted); margin-top: 3px; }
  .contact-list { list-style: none; margin-top: 14px; display: flex; flex-direction: column; gap: 6px; }
  .contact-list li { display: flex; align-items: center; gap: 8px; font-size: 8px; color: var(--ink); white-space: nowrap; }
  .contact-list svg { width: 9px; height: 9px; fill: var(--charcoal); flex: none; }
  .front-band { position: absolute; left: 0; bottom: 0; width: 520px; height: 120px; }
  .address {
    position: absolute; right: 28px; bottom: 18px;
    font-size: 9px; color: var(--paper); letter-spacing: 0.5px;
  }
</style>
</head>
<body>

<section class="card card-back" aria-label="Business card back">
  <div class="brand">
    <div class="brand-row">
      <span class="brand-mark"></span>
      <span class="brand-name">Orvel Partners LLC</span>
    </div>
    <span class="brand-tagline">Business Consulting Advisory Group</span>
  </div>
</section>

<section class="card card-front" aria-label="Business card front">
  <div class="front-brand">
    <div class="brand-row">
      <span class="brand-mark"></span>
      <span class="brand-name">Orvel Partners LLC</span>
    </div>
    <span class="brand-tagline">Business Consulting Advisory Group</span>
  </div>

  <div class="contact">
    <p class="person-name">Tomas Wenholt</p>
    <p class="person-role">Director</p>
    <ul class="contact-list">
      <li><svg viewBox="0 0 10 10"><path d="M2 0.5 L3.6 0.5 L4.3 2.8 L3.2 3.7 C3.8 5 4.9 6.1 6.3 6.8 L7.2 5.7 L9.5 6.4 L9.5 8 C9.5 9 8.7 9.5 8 9.5 C4 9.3 0.7 6 0.5 2 C0.5 1.2 1.1 0.5 2 0.5 Z"/></svg>+1 302 555 0148</li>
      <li><svg viewBox="0 0 10 10"><path d="M2 0.5 L3.6 0.5 L4.3 2.8 L3.2 3.7 C3.8 5 4.9 6.1 6.3 6.8 L7.2 5.7 L9.5 6.4 L9.5 8 C9.5 9 8.7 9.5 8 9.5 C4 9.3 0.7 6 0.5 2 C0.5 1.2 1.1 0.5 2 0.5 Z"/></svg>+1 302 555 0176</li>
      <li><svg viewBox="0 0 10 10"><path d="M0.5 2 H9.5 V8.5 H0.5 Z M1 2.4 L5 5.6 L9 2.4" stroke="#fff" stroke-width="0.8"/></svg>tomas@orvel-advisory.com</li>
      <li><svg viewBox="0 0 10 10"><circle cx="5" cy="5" r="4.5"/><path d="M0.5 5 H9.5 M5 0.5 C3 3 3 7 5 9.5 M5 0.5 C7 3 7 7 5 9.5" stroke="#fff" stroke-width="0.7" fill="none"/></svg>www.orvel-advisory.com</li>
    </ul>
  </div>

  <svg class="front-band" viewBox="0 0 520 120" preserveAspectRatio="none" aria-hidden="true">
    <path d="M0 58 C170 78 360 50 520 4 L520 120 L0 120 Z" fill="var(--gold)"/>
    <path d="M0 66 C170 86 360 60 520 16 L520 120 L0 120 Z" fill="var(--paper)"/>
    <path d="M0 72 C170 92 360 68 520 24 L520 120 L0 120 Z" fill="var(--charcoal)"/>
  </svg>
  <p class="address">48215 Ridgefern Road, Dunmore, DE 19872 USA</p>
</section>

</body>
</html>
```